Business Card Design

New Homes
Renovations/Additions
Building Maintenance
Design
Council Approvals
Estimates
Project and Construction Management

The back of the card should only contain my logo which is attached and under the logo have written velta & velta constructions.

Industry/Entity Type

Business

Contact Information for Business Card

Company Name: Velta & Velta Constructions Pty Ltd
BLD 613072
ABN: 42 905 217 630
Position: Director
Name: Tarv Olukendri
Tel: m. 0418276034
f. (08)83126649
veltanvelta@mailpost.example

```html
<!DOCTYPE html>
<html lang="en">
<head>
<meta charset="utf-8">
<title>Velta &amp; Velta Constructions — Business Card</title>
<link rel="stylesheet" href="https://fonts.googleapis.com/css2?family=Inter:wght@300;400&family=Libre+Baskerville:ital@0;1&display=swap">
<style>
  :root {
    --backdrop: #e4e4e4;
    --card: #ffffff;
    --ink: #1c1c1c;
    --ink-soft: #4a4a4a;
    --ink-muted: #8a8a8a;
    --edge: #d6d6d6;
  }
  * { box-sizing: border-box; margin: 0; padding: 0; }
  html, body {
    width: 1200px; height: 800px; overflow: hidden;
    background: var(--backdrop);
  }
  .canvas {
    position: relative; width: 1200px; height: 800px;
  }
  .card {
    position: absolute; top: 252px;
    width: 520px; height: 297px;
    background: var(--card);
    border: 1px solid var(--edge);
    box-shadow: 0 10px 28px rgba(0,0,0,0.12);
  }
  .card--front { left: 50px; }
  .card--back { left: 630px; }

  .brand-mark {
    position: absolute;
    display: flex; align-items: center; gap: 10px;
    font-family: "Libre Baskerville", serif;
    font-weight: 400;
    color: var(--ink);
  }
  .brand-mark__dot {
    width: 22px; height: 22px; border-radius: 50%;
    border: 2px solid var(--ink);
    flex: none;
  }
  .card--front .brand-mark { left: 34px; top: 62px; font-size: 17px; }
  .card--back .brand-mark {
    left: 0; right: 0; top: 92px; justify-content: center; font-size: 26px;
  }

  .holder {
    position: absolute; left: 250px; top: 62px;
    font-family: "Inter", sans-serif; font-weight: 300;
  }
  .holder__name {
    font-size: 19px; letter-spacing: 0.02em; color: var(--ink-soft);
    text-transform: uppercase;
  }
  .holder__role { font-size: 12px; color: var(--ink-muted); margin-top: 3px; }

  .contact {
    position: absolute; left: 186px; top: 148px;
    list-style: none;
    font-family: "Inter", sans-serif; font-weight: 300;
    font-size: 13.5px; line-height: 21px; color: var(--ink-soft);
  }

  .tagline {
    position: absolute; left: 0; right: 0; top: 168px;
    text-align: center;
    font-family: "Libre Baskerville", serif; font-style: italic;
    font-size: 17px; color: var(--ink-soft);
  }
</style>
</head>
<body>
<main class="canvas">
  <section class="card card--front" aria-label="Business card front">
    <div class="brand-mark"><span class="brand-mark__dot"></span><span>Velta &amp; Velta</span></div>
    <div class="holder">
      <p class="holder__name">Tarv Olukendri</p>
      <p class="holder__role">Director</p>
    </div>
    <ul class="contact">
      <li>BLD 613072</li>
      <li>ABN: 42 905 217 630</li>
      <li>Tel: 0418276034</li>
      <li>Fax: (08)83126649</li>
      <li>veltanvelta@mailpost.example</li>
    </ul>
  </section>

  <section class="card card--back" aria-label="Business card back">
    <div class="brand-mark"><span class="brand-mark__dot"></span><span>Velta &amp; Velta</span></div>
    <p class="tagline">Velta &amp; Velta Constructions</p>
  </section>
</main>
</body>
</html>
```